Records Management Company Revamp

We are looking to revamp our web presence, and need a catchy design that helps us to get noticed! We would like the website to be in wordpress. the main requirements are a home page, a landing page template for SEO / PPC, and then a few other pages that can be reused throughout the website.

We are happy to supply content / video etc.
Updates

Low designer entries

Have guaranteed payment and hoping to receive more designs

Number of Pages Required

3 page

Other font styles liked:
• Find fonts listed in attached branding document

Requirements
Must have
• Home page as well as sub pages according to their colours. Need to use colours and fonts set out in branding guide. Attached are examples of home page and sub pages.
Nice to have
• We have uploaded some very basic ideas we have of how we wish the website to look, but looking to have it more professional and fit together. Please see uploaded items.

```html
<!DOCTYPE html>
<html lang="en">
<head>
<meta charset="utf-8">
<title>Vault Keep – Archive Document Storage</title>
<link href="https://fonts.googleapis.com/css2?family=Raleway:wght@300;400;500;600&family=Open+Sans:wght@400;600;700&display=swap" rel="stylesheet">
<style>
:root{
  --blue:#1e9ce0;
  --blue-dark:#0f6fb5;
  --green-a:#5dbb1f;
  --green-b:#b8df1a;
  --purple-a:#7b4fc8;
  --purple-b:#4a2a9a;
  --yellow-a:#f7cf22;
  --yellow-b:#f5960e;
  --ink:#1f1f1f;
  --grey:#8a8a8a;
  --light:#f3f3f3;
  --dark:#1b1b1b;
  --orange:#ef8a1c;
  --white:#fff;
}
*{box-sizing:border-box;margin:0;padding:0}
html,body{width:1200px;height:3579px;overflow:hidden}
body{position:relative;background:var(--white);font-family:"Open Sans",Arial,sans-serif;color:var(--ink)}
.abs{position:absolute}
.btn-green{position:absolute;background:linear-gradient(90deg,var(--green-a),var(--green-b));color:#123;border-radius:4px;font-size:13px;display:flex;align-items:center;justify-content:center}
h2.section-title{position:absolute;left:0;width:1200px;text-align:center;font-family:"Raleway",sans-serif;font-weight:400;font-size:40px;letter-spacing:2px;color:var(--ink)}
h2.section-title span{display:inline-block;width:56px;height:3px;background:var(--ink);vertical-align:middle;margin:0 18px}
.section-sub{position:absolute;left:300px;width:600px;text-align:center;font-size:13.5px;line-height:1.5;color:#333}

/* hero */
.hero-photo{left:0;top:0;width:1200px;height:716px;background:linear-gradient(90deg,rgba(40,150,225,.95) 0%,rgba(120,180,225,.55) 35%,rgba(200,210,225,.45) 60%,rgba(150,150,200,.6) 100%)}
.hero-fade{left:0;top:420px;width:1200px;height:300px;background:linear-gradient(180deg,rgba(255,255,255,0),#fff 95%)}
.brand{left:52px;top:36px;display:flex;align-items:center;gap:10px;color:var(--white);font-family:"Raleway",sans-serif;font-weight:600;font-size:34px;line-height:1}
.brand i{display:block;width:26px;height:26px;background:var(--white)}
.nav{left:432px;top:58px;display:flex;gap:30px;font-size:14.5px;color:#333;align-items:center}
.nav .active{color:#2c6d1c;border-bottom:2px solid var(--green-a);padding-bottom:4px}
.nav .cta{background:linear-gradient(90deg,var(--green-a),var(--green-b));padding:5px 14px;border-radius:14px;color:#1a3a08}
.hero-title{left:48px;top:300px;font-family:"Raleway",sans-serif;font-weight:400;font-size:44px;line-height:50px;color:#2a2a2a;border-left:5px solid var(--green-a);padding-left:0;margin-left:-14px;padding-left:9px}
.hero-text{left:48px;top:412px;font-size:13px;color:#222}
.cart{left:615px;top:430px;width:172px;height:262px;background:linear-gradient(180deg,#d8a866,#b78345 70%,#444);border-radius:6px}
.form-panel{left:763px;top:162px;width:411px;height:494px;background:linear-gradient(160deg,var(--purple-a),var(--purple-b));box-shadow:0 8px 24px rgba(0,0,0,.3)}
.ribbon{left:795px;top:208px;width:342px;height:54px;background:var(--blue);color:var(--white);font-family:"Raleway",sans-serif;font-size:27px;font-weight:500;display:flex;align-items:center;justify-content:center}
.ribbon-tail{top:208px;width:0;height:0;border-top:27px solid var(--blue-dark);border-bottom:27px solid var(--blue-dark)}
.form-note{left:815px;top:268px;font-size:10.5px;color:#e6dcf7}
.field{left:815px;width:320px;border-bottom:1px solid rgba(255,255,255,.55);color:#e9e2f8;font-size:14px;padding-bottom:8px}
.submit{left:815px;top:582px;width:147px;height:38px;border-radius:6px;background:linear-gradient(180deg,var(--yellow-a),var(--yellow-b));display:flex;align-items:center;justify-content:center;font-size:14px;color:#3a2500}

/* offer cards */
.offer-card{width:539px;height:294px;overflow:hidden}
.offer-card .label{position:absolute;left:0;top:187px;background:rgba(255,255,255,.82);font-family:"Raleway",sans-serif;font-size:28px;letter-spacing:1px;padding:2px 8px 0 18px;color:#222}
.offer-card .band{position:absolute;left:0;top:226px;width:100%;height:56px;background:rgba(20,20,30,.55);color:#eee;font-size:11.5px;line-height:14px;padding:5px 80px 0 18px}
.offer-card .go{position:absolute;right:18px;top:237px;width:30px;height:30px}

/* how it works */
.how-bg{left:0;top:1606px;width:1200px;height:620px;background:var(--light)}
.step-card{left:496px;top:1887px;width:205px;height:260px;background:var(--white);box-shadow:0 2px 10px rgba(0,0,0,.08)}
.step{width:224px;text-align:center}
.step .icon{width:114px;height:114px;border-radius:50%;background:var(--blue);margin:0 auto;display:flex;align-items:center;justify-content:center}
.step h3{margin-top:60px;font-size:15px;line-height:18px;font-weight:700;color:#222}
.step p{margin:18px auto 0;width:150px;font-size:10.5px;line-height:13px;color:#999}
.step .btn-green{position:relative;width:148px;height:32px;margin:20px auto 0;font-size:11px}

/* team */
.team-photo{left:0;top:2226px;width:553px;height:704px;background:linear-gradient(100deg,#3a3a42 0%,#5b5046 40%,#8f8a84 75%,#fff 100%)}
.team-title{left:589px;top:2290px;font-family:"Raleway",sans-serif;font-size:40px;letter-spacing:1px;color:#222}
.team-rule{left:983px;top:2316px;width:217px;height:4px;background:#333}
.team-text{left:589px;top:2364px;width:560px;font-size:12.5px;line-height:18px;color:#999}
.member{width:200px;text-align:center}
.member .avatar{width:134px;height:134px;border-radius:50%;margin:0 auto;border:5px solid #eee;background:linear-gradient(160deg,#c9b4a0,#6e5a4b)}
.member b{display:block;margin-top:14px;font-family:"Raleway",sans-serif;font-weight:500;font-size:21px;color:#222}
.member span{font-size:12px;color:#999}

/* testimonials */
.clients-bg{left:0;top:2930px;width:1200px;height:649px;background:linear-gradient(135deg,#2a2a2a,#141414 60%,#222)}
.clients-title{left:0;top:2992px;width:1200px;text-align:center;color:var(--white);font-family:"Raleway",sans-serif;font-size:38px;letter-spacing:1px}
.quote-card{background:var(--white);border-radius:4px;text-align:center;box-shadow:0 6px 20px rgba(0,0,0,.4)}
.quote-card .avatar{position:absolute;left:50%;transform:translateX(-50%);border-radius:50%;border:4px solid #fff;background:linear-gradient(160deg,#b58f72,#5a3f2e)}
.quote-card b{display:block;font-size:16px;font-weight:700;color:#111}
.quote-card em{display:block;font-size:11px;color:var(--orange);font-style:normal;margin-top:4px}
.quote-card p{text-align:left;color:#222;position:relative}
.quote-card p::before{content:"\201C";position:absolute;left:-22px;top:-8px;font-size:40px;color:#ccc;font-family:Georgia,serif}
.quote-card p::after{content:"\201D";position:absolute;right:-14px;bottom:-36px;font-size:40px;color:#ccc;font-family:Georgia,serif}
.arrow{color:var(--orange);font-size:26px;font-weight:700}
</style>
</head>
<body>

<!-- hero -->
<div class="abs hero-photo" role="img" aria-label="Office workers handling archive files, tinted blue"></div>
<div class="abs hero-fade"></div>
<div class="abs brand"><i></i>Vault Keep</div>
<nav class="abs nav">
  <span class="active">Home</span><span>Offsite Storage</span><span>Document Shredding</span><span>Digitisation</span><span>Archive Supplies</span><span class="cta">Contact Us</span>
</nav>
<h1 class="abs hero-title">ARCHIVE DOCUMENT STORAGE<br>&amp; RECORDS MANAGEMENT</h1>
<p class="abs hero-text">Professional, secure and reliable. Vault Keep is your new home for all your archiving needs.</p>
<div class="btn-green" style="left:48px;top:449px;width:178px;height:36px">Contact Us</div>

<div class="abs form-panel"></div>
<div class="abs ribbon-tail" style="left:763px;border-left:16px solid transparent"></div>
<div class="abs ribbon-tail" style="left:1137px;border-right:16px solid transparent"></div>
<div class="abs ribbon">Price Calculator Form</div>
<p class="abs form-note">Find out how cost effective we are in storing your archive boxes.</p>
<div class="abs field" style="top:312px">Name:</div>
<div class="abs field" style="top:379px">Email Address:</div>
<div class="abs field" style="top:446px">Subject:</div>
<div class="abs field" style="top:513px">Approx. Number of boxes:</div>
<div class="abs submit">Submit</div>
<div class="abs cart" role="img" aria-label="Hand truck carrying stacked cardboard archive boxes"></div>

<!-- what we offer -->
<h2 class="section-title" style="top:760px"><span></span>WHAT WE OFFER<span></span></h2>
<p class="section-sub" style="top:818px">Finding a Mentor used to be hard; but not any more. We've turned the traditional model on its head, so now Mentors seek you</p>

<div class="abs offer-card" style="left:48px;top:911px" role="img" aria-label="Warehouse aisle with shelving for offsite storage">
  <div class="abs" style="inset:0;background:linear-gradient(135deg,#1d4f8a,#4a7fb8 50%,#9dbad6)"></div>
  <div class="label">OFFSITE STORAGE</div>
  <div class="band">Imagine being able to speak to someone who has been through the challenges you are currently facing? Who has "been there seen that" and can help you navigate the ups and downs of your career or business?</div>
  <svg class="go" viewBox="0 0 30 30"><circle cx="15" cy="15" r="13" fill="none" stroke="#fff" stroke-width="2"/><path d="M13 9l6 6-6 6" fill="none" stroke="#fff" stroke-width="2.5"/></svg>
</div>
<div class="abs offer-card" style="left:606px;top:911px" role="img" aria-label="Shredded paper spilling from a shredder bin">
  <div class="abs" style="inset:0;background:linear-gradient(135deg,#8a8f94,#c7c9c6 55%,#d6cf90)"></div>
  <div class="label">DOCUMENT SHREDDING</div>
  <div class="band">Imagine being able to speak to someone who has been through the challenges you are currently facing? Who has "been there seen that" and can help you navigate the ups and downs of your career or business?</div>
  <svg class="go" viewBox="0 0 30 30"><circle cx="15" cy="15" r="13" fill="none" stroke="#fff" stroke-width="2"/><path d="M13 9l6 6-6 6" fill="none" stroke="#fff" stroke-width="2.5"/></svg>
</div>
<div class="abs offer-card" style="left:48px;top:1229px" role="img" aria-label="Hands feeding a document into a scanner">
  <div class="abs" style="inset:0;background:linear-gradient(135deg,#6f767d,#c8ccd0 55%,#9aa0a6)"></div>
  <div class="label">DIGITISATION</div>
  <div class="band">Imagine being able to speak to someone who has been through the challenges you are currently facing? Who has "been there seen that" and can help you navigate the ups and downs of your career or business?</div>
  <svg class="go" viewBox="0 0 30 30"><circle cx="15" cy="15" r="13" fill="none" stroke="#fff" stroke-width="2"/><path d="M13 9l6 6-6 6" fill="none" stroke="#fff" stroke-width="2.5"/></svg>
</div>
<div class="abs offer-card" style="left:606px;top:1229px" role="img" aria-label="Camera and office supplies on a desk">
  <div class="abs" style="inset:0;background:linear-gradient(135deg,#8b7c8f,#b7a7b2 50%,#5e4f5a)"></div>
  <div class="label">ARCHIVING SUPPLIES</div>
  <div class="band">Imagine being able to speak to someone who has been through the challenges you are currently facing? Who has "been there seen that" and can help you navigate the ups and downs of your career or business?</div>
  <svg class="go" viewBox="0 0 30 30"><circle cx="15" cy="15" r="13" fill="none" stroke="#fff" stroke-width="2"/><path d="M13 9l6 6-6 6" fill="none" stroke="#fff" stroke-width="2.5"/></svg>
</div>

<!-- how it works -->
<div class="abs how-bg"></div>
<h2 class="section-title" style="top:1662px"><span></span>HOW IT WORKS<span></span></h2>
<p class="section-sub" style="top:1718px">Finding a Mentor used to be hard; but not any more. We've turned the traditional model on its head, so now Mentors seek you</p>
<div class="abs step-card"></div>

<div class="abs step" style="left:36px;top:1823px">
  <div class="icon"><svg width="60" height="60" viewBox="0 0 60 60" fill="none" stroke="#fff" stroke-width="3"><path d="M10 22h40v28H10z"/><path d="M10 22l-6-10h22l4 10M50 22l6-10H34l-4 10M30 22v28"/></svg></div>
  <h3>We Deliver Boxes<br>And Barcodes</h3>
  <p>If you need them, we get you started with all the essentials to prepare your archives.</p>
  <div class="btn-green">Contact Us</div>
</div>
<div class="abs step" style="left:260px;top:1823px">
  <div class="icon"><svg width="56" height="56" viewBox="0 0 56 56" fill="none" stroke="#fff" stroke-width="3"><rect x="8" y="14" width="40" height="34"/><path d="M8 14l6-8h28l6 8M22 24h12"/></svg></div>
  <h3>We Pick Up Your<br>Documents</h3>
  <p>If you need them, we get you started with all the essentials to prepare your archives.</p>
  <div class="btn-green">Contact Us</div>
</div>
<div class="abs step" style="left:484px;top:1823px">
  <div class="icon"><svg width="56" height="56" viewBox="0 0 56 56" fill="none" stroke="#fff" stroke-width="3"><rect x="10" y="6" width="36" height="44"/><path d="M10 20h36M10 35h36M24 13h8M24 27h8M24 42h8"/></svg></div>
  <h3>We Store Your<br>Documents</h3>
  <p>If you need them, we get you started with all the essentials to prepare your archives.</p>
  <div class="btn-green">Contact Us</div>
</div>
<div class="abs step" style="left:709px;top:1823px">
  <div class="icon"><svg width="56" height="56" viewBox="0 0 56 56" fill="#fff"><path d="M6 27L50 8 42 48 28 38 22 46 20 33 42 15 17 30z"/></svg></div>
  <h3>We Retrieve &amp; Deliver<br>Your Documents</h3>
  <p>If you need them, we get you started with all the essentials to prepare your archives.</p>
  <div class="btn-green">Contact Us</div>
</div>
<div class="abs step" style="left:933px;top:1823px">
  <div class="icon"><svg width="56" height="56" viewBox="0 0 56 56" fill="none" stroke="#fff" stroke-width="3"><path d="M10 12h36M22 12V7h12v5M14 12l3 38h22l3-38M23 20v24M28 20v24M33 20v24"/></svg></div>
  <h3>We Can Securely<br>Destroy</h3>
  <p>If you need them, we get you started with all the essentials to prepare your archives.</p>
  <div class="btn-green">Contact Us</div>
</div>
<svg class="abs" style="left:640px;top:2100px" width="20" height="26" viewBox="0 0 20 26"><path d="M4 2v17l4-4 3 8 3-1-3-8h6z" fill="#fff" stroke="#222" stroke-width="1.5"/></svg>

<!-- team -->
<div class="abs team-photo" role="img" aria-label="Business team reviewing documents at a table"></div>
<h2 class="abs team-title">THE VAULT TEAM</h2>
<div class="abs team-rule"></div>
<p class="abs team-text">Guide Link changes all that, levelling the playing field and making it easy for entrepreneurs and professionals to find the advice and guidance they deserve.</p>

<div class="abs member" style="left:563px;top:2457px"><div class="avatar" role="img" aria-label="Team member portrait"></div><b>Morgan Hale</b><span>Creative Director</span></div>
<div class="abs member" style="left:764px;top:2457px"><div class="avatar" role="img" aria-label="Team member portrait"></div><b>Morgan Hale</b><span>Creative Director</span></div>
<div class="abs member" style="left:964px;top:2457px"><div class="avatar" role="img" aria-label="Team member portrait"></div><b>Morgan Hale</b><span>Creative Director</span></div>
<div class="abs member" style="left:563px;top:2689px"><div class="avatar" role="img" aria-label="Team member portrait"></div><b>Morgan Hale</b><span>Creative Director</span></div>
<div class="abs member" style="left:764px;top:2689px"><div class="avatar" role="img" aria-label="Team member portrait"></div><b>Morgan Hale</b><span>Creative Director</span></div>
<div class="abs member" style="left:964px;top:2689px"><div class="avatar" role="img" aria-label="Team member portrait"></div><b>Morgan Hale</b><span>Creative Director</span></div>

<!-- testimonials -->
<div class="abs clients-bg"></div>
<h2 class="abs clients-title">WHAT OUR CLIENTS SAY</h2>
<div class="abs arrow" style="left:44px;top:3288px">&lsaquo;</div>
<div class="abs arrow" style="left:1136px;top:3288px">&rsaquo;</div>

<div class="abs quote-card" style="left:86px;top:3190px;width:284px;height:275px">
  <div class="avatar" role="img" aria-label="Client portrait" style="top:-45px;width:96px;height:96px"></div>
  <b style="margin-top:64px">CLARA BENTON</b><em>HARBOR TRUST COMPANY</em>
  <p style="margin:22px 40px 0 60px;font-size:13px;line-height:16px">Without ArcFile I would have to hire 2-3 more employees to keep up with the demand of keying lines in. The customer support staff has been GREAT to work with. It's hard to imagine life without ArcFile. They have certainly made my life easier!</p>
</div>
<div class="abs quote-card" style="left:430px;top:3157px;width:334px;height:346px">
  <div class="avatar" role="img" aria-label="Client portrait" style="top:-52px;width:106px;height:106px"></div>
  <b style="margin-top:72px;font-size:18px">CLARA BENTON</b><em style="font-size:12.5px">HARBOR TRUST COMPANY</em>
  <p style="margin:30px 44px 0 34px;font-size:16px;line-height:20px">Without ArcFile I would have to hire 2-3 more employees to keep up with the demand of keying lines in. The customer support staff has been GREAT to work with. It's hard to imagine life without ArcFile. They have certainly made my life easier!</p>
</div>
<div class="abs quote-card" style="left:828px;top:3190px;width:284px;height:275px">
  <div class="avatar" role="img" aria-label="Client portrait" style="top:-45px;width:96px;height:96px"></div>
  <b style="margin-top:64px">CLARA BENTON</b><em>HARBOR TRUST COMPANY</em>
  <p style="margin:22px 40px 0 60px;font-size:13px;line-height:16px">Without ArcFile I would have to hire 2-3 more employees to keep up with the demand of keying lines in. The customer support staff has been GREAT to work with. It's hard to imagine life without ArcFile. They have certainly made my life easier!</p>
</div>

</body>
</html>
```